Technology Model Graphic for School District

We need a graphic (to be used as a poster, on our website, as a 1-page overview, etc.) that portrays our school (K-12) district's vision for technology in schools. There are 5 components to our vision:
--Access & Equity (could be split into two separate components if that worked better for the design),
--Sustainability,
--Bright Path Skills (district specific: you can read about them here: https://sites.brambleweb.org/larkvalesd.us/brightpathskills/home),
--Empowered Learning,
--Bright Path Compass (district specific: our goal to have every student graduate with a viable and valued plan for what they do after high school graduation).

We also would somehow like to incorporate our district logo (included).

We would like a design that works fine by itself (just the components in the design) AND one that incorporates the descriptions as well (for instance as a one-page overview or poster)).

One idea we think may have potential is somehow incorporating the components of our vision into some sort of digital tree--incorporating the idea of technology (circuitry/connections/"branches"/etc.) with the idea of a tree to connote growth/learning/ etc. A Google image search of “digital tree images” gives an idea. We would like it to have a tech feel, but also be friendly and warm. We do not want something cartoonish or cute. We are not wedded to the idea of a digital tree--it’s just an idea. I have included a PowerPoint and PDF of some of the designs that have been floated just so you can see the gist. Of course, we're turning to you for this project because ultimately these designs do not inspire.

The components are all essential to our vision and are not hierarchical. However, Access, Equity, and Sustainability are the components that drive and/or support the other three (Empowered Learning, Bright Path Skills and Bright Path Compass).

Components
Access & Equity*: Students and staff have the tools, skills, and opportunities to leverage technology to improve learning and productivity. Efforts ensure that initiatives acknowledge and support the needs of different students, staff members, classrooms, and buildings in an equitable way.

Sustainability: Technology decisions are made considering identified aspects of sustainability and align to district goals and priorities.

Empowered Learning: Technology is used in authentic ways to design experiences that challenge, engage and empower students to deeper levels of learning and demonstrating that learning.

Bright Path Skills: Students skillfully use digital tools to support and reflect upon their acquisition and demonstration of the Bright Path Skills both inside and outside of school.

Bright Path Compass: Throughout elementary, middle, and high school, students build a vision for their valued, viable, and successful future--actively exploring, refining and planning their next steps.

This document may be useful for you in understanding each of these components a bit more: https://lnk.quorvo.io/K3pzQ8

*If Access & Equity get split apart then the first sentence goes with Access and the second sentence goes with Equity.

```html
<!DOCTYPE html>
<html lang="en">
<head>
<meta charset="utf-8">
<title>Larkvale – Bright Path Students</title>
<link rel="stylesheet" href="https://fonts.googleapis.com/css2?family=Arimo:ital,wght@0,400;0,700;1,400;1,700&family=Varela+Round&family=Fjalla+One&display=swap">
<style>
  :root{
    --blue:#0b3dff;
    --navy:#1c1f8c;
    --yellow:#f6ee00;
    --ink:#141414;
    --sky-top:#c9f0fb;
    --white:#ffffff;
  }
  *{margin:0;padding:0;box-sizing:border-box}
  html,body{width:849px;height:1200px;overflow:hidden;background:var(--white)}
  .poster{position:relative;width:849px;height:1200px;overflow:hidden;
    background:
      radial-gradient(ellipse 260px 520px at 425px 700px, rgba(246,238,0,.28), rgba(246,238,0,0) 70%),
      linear-gradient(100deg, #9fd3f3 0%, var(--sky-top) 30%, #d6f6fc 55%, var(--sky-top) 75%, #a9d8f4 100%);
    font-family:"Varela Round", sans-serif;color:var(--ink)}
  .poster::after{content:"";position:absolute;inset:0;
    background:linear-gradient(180deg, rgba(143,169,232,0) 55%, rgba(143,169,232,.75) 100%);pointer-events:none}

  .column{position:absolute;top:310px;width:224px;height:498px;z-index:1;
    background:linear-gradient(180deg,rgba(255,255,255,.15),rgba(255,255,255,.55))}
  .column--a{left:57px}
  .column--b{left:313px}
  .column--c{left:566px}

  .pillar{position:absolute;top:890px;height:310px;z-index:2;
    background:linear-gradient(180deg,rgba(255,255,255,.88),rgba(255,255,255,.35))}
  .pillar--access{left:48px;width:232px}
  .pillar--sustain{left:306px;width:231px}
  .pillar--equity{left:566px;width:231px}

  .header-arc{position:absolute;left:-230px;top:-420px;width:1309px;height:742px;border-radius:50%;background:var(--white);z-index:3}
  .brand{position:absolute;left:0;top:70px;width:849px;text-align:center;z-index:4}
  .brand__name{font-family:"Arimo",sans-serif;font-weight:700;font-size:98px;line-height:1;color:var(--blue);letter-spacing:2px}
  .brand__name::before{content:"";display:inline-block;width:22px;height:22px;background:var(--yellow);margin-right:14px;vertical-align:middle}
  .brand__tagline{font-size:47px;color:var(--blue);margin-top:10px;letter-spacing:1px}

  .arc-title{position:absolute;left:0;top:340px;width:849px;height:120px;z-index:4}
  .arc-title text{font-family:"Arimo",sans-serif;font-weight:700;font-style:italic;font-size:22px;fill:var(--navy);letter-spacing:12px}

  .component{position:absolute;z-index:5;display:flex;flex-direction:column;align-items:center}
  .component--learning{left:70px;top:480px;width:200px}
  .component--compass{left:323px;top:402px;width:204px}
  .component--skills{left:576px;top:470px;width:204px}
  .component__art{width:150px;border-radius:10px}
  .component--learning .component__art{height:120px;background:linear-gradient(180deg,#5a6ad0,#f6ee00)}
  .component--compass .component__art{height:135px;background:linear-gradient(180deg,#f6ee00,#7fa6f2)}
  .component--skills .component__art{height:125px;background:linear-gradient(180deg,#f6ee00,#0b3dff)}
  .component__label{margin-top:12px;font-family:"Fjalla One",sans-serif;font-size:17px;line-height:20px;color:var(--navy);text-align:center}
  .component__district{font-family:"Arimo",sans-serif;font-weight:700;font-size:10px;color:var(--navy);text-align:center;margin-top:2px}

  .summary{position:absolute;z-index:5;font-size:14.8px;line-height:18.8px;text-align:justify;text-indent:12px;letter-spacing:.3px;hyphens:auto;-webkit-hyphens:auto}
  .summary--learning{left:61px;top:671px;width:216px}
  .summary--compass{left:324px;top:644px;width:198px}
  .summary--skills{left:571px;top:671px;width:214px}

  .section-title{position:absolute;left:0;top:848px;width:849px;text-align:center;z-index:5;
    font-family:"Arimo",sans-serif;font-weight:700;font-style:italic;font-size:23px;color:var(--blue);letter-spacing:14px}

  .pillar__title{position:absolute;z-index:5;top:896px;text-align:center;font-family:"Arimo",sans-serif;font-weight:700;font-size:19.5px;color:var(--blue);letter-spacing:1.5px}
  .pillar__text{position:absolute;z-index:5;top:940px;font-size:16px;line-height:20.6px;text-align:justify;text-indent:12px;letter-spacing:.4px;hyphens:auto;-webkit-hyphens:auto}
  .pillar__title--access,.pillar__text--access{left:51px;width:226px}
  .pillar__title--sustain,.pillar__text--sustain{left:309px;width:226px}
  .pillar__title--equity,.pillar__text--equity{left:571px;width:222px}

  .footer-arc{position:absolute;left:198px;top:1083px;width:448px;height:300px;border-radius:50%;background:var(--white);z-index:6}
  .footer-note{position:absolute;left:268px;top:1138px;width:314px;text-align:center;z-index:7;
    font-family:"Arimo",sans-serif;font-style:italic;font-size:13.5px;line-height:16.6px;color:var(--blue);letter-spacing:.5px}
</style>
</head>
<body>
<main class="poster">
  <div class="column column--a"></div>
  <div class="column column--b"></div>
  <div class="column column--c"></div>

  <div class="header-arc"></div>
  <header class="brand">
    <h1 class="brand__name">LARKVALE</h1>
    <p class="brand__tagline">Bright Path Students</p>
  </header>

  <svg class="arc-title" viewBox="0 340 849 120" aria-label="Lifelong personal success">
    <defs><path id="success-arc" d="M95 437 Q425 300 760 432"/></defs>
    <text><textPath href="#success-arc" startOffset="50%" text-anchor="middle">LIFELONG PERSONAL SUCCESS</textPath></text>
  </svg>

  <div class="component component--learning">
    <div class="component__art" role="img" aria-label="Emblem artwork: light bulb, gears and an open book"></div>
    <p class="component__label">EMPOWERED LEARNING</p>
    <p class="component__district">Larkvale School District</p>
  </div>
  <div class="component component--compass">
    <div class="component__art" role="img" aria-label="Emblem artwork: graduate with arrows rising upward"></div>
    <p class="component__label">BRIGHT PATH COMPASS</p>
    <p class="component__district">Larkvale School District</p>
  </div>
  <div class="component component--skills">
    <div class="component__art" role="img" aria-label="Emblem artwork: upward arrow with a mortarboard"></div>
    <p class="component__label">BRIGHT PATH SKILLS</p>
    <p class="component__district">Larkvale School District</p>
  </div>

  <p class="summary summary--learning">Technology is used in authentic ways to design experiences that challenge, engage and empower students to deeper levels of learning and demonstrating that learning.</p>
  <p class="summary summary--compass">Throughout elementary, middle, and high school, students build a vision for their valued, viable, and successful future--actively exploring, refining and planning their next steps.</p>
  <p class="summary summary--skills">Students skillfully use digital tools to support and reflect upon their acquisition and demonstration of the Bright Path Skills both inside and outside of school.</p>

  <h2 class="section-title">TOOLS AND EXPERIENCES</h2>

  <div class="pillar pillar--access"></div>
  <div class="pillar pillar--sustain"></div>
  <div class="pillar pillar--equity"></div>

  <h3 class="pillar__title pillar__title--access">ACCESS</h3>
  <p class="pillar__text pillar__text--access">Students and staff have the tools, skills, and opportunities to leverage technology to improve learning and productivity.</p>
  <h3 class="pillar__title pillar__title--sustain">SUSTAINABILITY</h3>
  <p class="pillar__text pillar__text--sustain">Technology decisions are made considering identified aspects of sustainability and align to district goals and priorities.</p>
  <h3 class="pillar__title pillar__title--equity">EQUITY</h3>
  <p class="pillar__text pillar__text--equity">Efforts ensure that initiatives support the diverse/particular needs of different students, staff members, classrooms, and buildings in an equitable way.</p>

  <div class="footer-arc"></div>
  <p class="footer-note">Together provide the tools and experiences necessary to create an individual, viable, and valued path to lifelong personal success.</p>
</main>
</body>
</html>
```